Expanding the consciousness of Humanity - Solvane-Harbor

Please note that whoever will win this project , a 1on1 Powerpoint design project will separately be launched and will be offered to the winning designer.

---------
This letterhead is to provide proposals, as well as manuals for my clients.

I am looking for the letter, power point design and business card that inspires people when they see it, that they feel that design has been done with love and passion. Something that is professional, simple and yet creative, Business like, yet spiritual. That inspires growth!

This part of the branding for my company, therefore the business card as well as the power point design that will come after as 1on1 project should have the same team and feeling.

Solvane harbor, The company will be providing Coaching services (one-one or groups) to corporations, teams and individuals, partnering with them to achieve their goals/vision, by helping them to remove the self-imposed limiting beliefs, helping them to get them out of their own way, helping them to raise their level of consciousness and self-awareness.

The vision is: Bring conscious leadership to the workplace and to individuals for the wellbeing of humanity.

I know that somewhere out there will resonate with this, and will be inspired to provide the best design :) thank you very much!!!!!

MPORTANT:
- To use Free Fonts - let me know where I can download them
- Editable formats please for the double sized business card

LOGO is attached in pdf. If needed other file type please let me know

Thank you thank you in advance for your time and inspiration!! Sending good vibes for a great design out there

Must Have:
- Please keep on mind that the cards - power point will have the same feeling - Corporate branding
- that is not to heavy to look at it, that is simple and beautiful and inspiring
- Looking to have Calibri or Calibri light font

imple, yet inspirational - Professional, yet playful - business like, yet spiritual

I am looking for something different that the "standard" designs out there.

For example, the Logo of the company in the back side with a quote and the front side something simple, yet inspiring. that has the contact info as well as the social media details LinkedIn - Facebook - tweeter - website

Open for suggestions and inspiration :)

Thank you!

Font styles to use
Sans Serif

Requirements
Must have
• - Please keep on mind that the cards - power point will have the same feeling
• - Corporate branding
• - that is not to heavy to look at it, that is simple and beautiful and inspiring
• - Looking to have Calibri or Calibri light font
• - Corporate colours as the logo

```html
<!DOCTYPE html>
<html lang="en">
<head>
<meta charset="utf-8">
<title>Solvane-Harbor Stationery</title>
<link href="https://fonts.googleapis.com/css2?family=Carlito:wght@400;700&display=swap" rel="stylesheet">
<style>
:root{
  --gold:#fbbd2e;
  --navy:#2f5690;
  --ink:#4a4a4a;
  --dark:#2b2b2b;
  --paper:#f8f8f8;
  --stage:#e9e9e9;
  --sig:#d9d9d9;
}
*{margin:0;padding:0;box-sizing:border-box}
html,body{width:1200px;height:1000px;overflow:hidden}
body{background:var(--stage);font-family:"Carlito",sans-serif;color:var(--ink);position:relative}
.sheet,.card{position:absolute;background:var(--paper);overflow:hidden}
.sheet{left:128px;top:60px;width:624px;height:880px}

.top-band{position:absolute;left:0;right:0;top:0;background:var(--gold)}
.top-line{position:absolute;left:0;right:0;background:var(--navy)}
.sheet .top-band{height:12px}
.sheet .top-line{top:16px;height:2px}

.brand{position:absolute;display:flex;align-items:center;white-space:nowrap}
.brand-dot{border-radius:50%;background:var(--gold);flex:none}
.brand-name{font-family:"Carlito",sans-serif;font-weight:700;color:var(--navy);letter-spacing:1px;line-height:1}
.brand-tag{font-family:"Carlito",sans-serif;color:var(--ink);letter-spacing:.8px;line-height:1}
.sheet .brand{left:48px;top:60px;gap:12px}
.sheet .brand-dot{width:46px;height:46px}
.sheet .brand-name{font-size:20px}
.sheet .brand-tag{font-size:9px;margin-top:5px}

.sender{position:absolute;left:354px;top:107px;font-size:9.5px;line-height:13px;color:var(--ink);white-space:nowrap}
.sender b,.sender .lbl{color:var(--navy);font-weight:700}
.sender b{font-size:10.5px}
.salutation{position:absolute;left:49px;top:218px;font-size:15px;font-weight:700;color:var(--dark)}
.body-copy{position:absolute;left:49px;top:254px;width:537px;font-size:11.6px;line-height:15.6px;text-align:justify}
.body-copy p{margin-bottom:15px}
.signature{position:absolute;left:47px;top:605px;width:98px;height:44px;background:linear-gradient(90deg,var(--sig),#ececec);border-radius:22px}

.socials{position:absolute;display:flex;gap:12px;font-size:9px;color:var(--ink);white-space:nowrap}
.sheet .socials{left:47px;top:846px}
.socials span{display:flex;align-items:center;gap:3px}
.ico{width:8px;height:8px;border-radius:50%;background:var(--navy);display:inline-block}
.rule{position:absolute;height:1px;background:var(--navy)}
.sheet .rule{left:0;right:0;top:859px}
.sheet .web{position:absolute;right:30px;top:853px;font-size:10px;color:var(--navy);letter-spacing:.3px;background:var(--paper);padding:0 4px}
.band{position:absolute;left:0;right:0;bottom:0;background:var(--gold)}
.sheet .band{height:9px}

.card{width:263px;height:151px}
.card-back{left:810px;top:618px;background:var(--gold)}
.card-back .brand{left:50%;top:62px;transform:translateX(-50%);gap:8px}
.card-back .brand-dot{width:20px;height:20px;background:var(--navy)}
.card-back .brand-name{font-size:13px;color:var(--navy)}
.card-back .web{position:absolute;left:0;right:0;top:136px;text-align:center;font-size:7px;color:#fff}

.card-front{left:810px;top:790px}
.card-front .top-band{height:5px}
.card-front .top-line{top:7px;height:1px}
.card-front .brand{left:12px;top:18px;gap:6px}
.card-front .brand-dot{width:18px;height:18px}
.card-front .brand-name{font-size:10px}
.card-front .brand-tag{font-size:5.5px;margin-top:2px}
.contact{position:absolute;right:16px;top:41px;text-align:right;font-size:6.8px;line-height:9.6px;white-space:nowrap}
.contact b{font-size:9px;color:var(--navy);display:block;line-height:12px}
.contact span{display:flex;justify-content:flex-end;align-items:center;gap:3px}
.contact .ico{width:6px;height:6px}
.card-front .socials{left:14px;top:106px;flex-direction:column;gap:1px;font-size:6.5px}
.card-front .socials .ico{width:5px;height:5px}
.card-front .rule{left:0;right:0;top:137px}
.card-front .tagline{position:absolute;right:16px;top:132px;font-size:6.5px;color:var(--navy);background:var(--paper);padding:0 3px;white-space:nowrap}
.card-front .band{height:7px}
</style>
</head>
<body>

<section class="sheet letterhead">
  <div class="top-band"></div>
  <div class="top-line"></div>
  <div class="brand">
    <span class="brand-dot"></span>
    <div>
      <div class="brand-name">SOLVANE-HARBOR</div>
      <div class="brand-tag">CLARITY - GROWTH - PURPOSE</div>
    </div>
  </div>
  <div class="sender">
    <b>Mireille Dostana,</b> MBA, MA, Beng, PCC<br>
    Business &amp; Corporate, Conscious Leadership Coaching<br>
    <span class="lbl">Tel:</span> 1 800 55 Canada &nbsp;<span class="lbl">Mail:</span> mireille@solvane-harbor.ca
  </div>

  <h1 class="salutation">Dear Mr. John,</h1>
  <div class="body-copy">
    <p>Lorem Ipsum is simply dummy text of the printing and typesetting industry. Lorem Ipsum has been the industry's standard dummy text ever since the 1500s, when an unknown printer took a galley of type and scrambled it to make a type specimen book. It has survived not only five centuries, but also the leap into electronic typesetting, remaining essentially unchanged.</p>
    <p>The standard chunk of Lorem Ipsum used since the 1500s is reproduced below for those interested. Sections 1.10.32 and 1.10.33 from "de Finibus Bonorum et Malorum" by Cicero are also reproduced in their exact original form, accompanied by English versions from the 1914 translation by H. Rackham</p>
    <p>Lorem Ipsum is simply dummy text of the printing and typesetting industry. Lorem Ipsum has been the industry's standard dummy text ever since the 1500s, when an unknown printer took a galley of type and scrambled it to make a type specimen book. It has survived not only five centuries, but also the leap into electronic typesetting, remaining essentially unchanged. It was popularised in the</p>
    <p>The standard chunk of Lorem Ipsum used since the 1500s is reproduced below for those interested. Sections 1.10.32 and 1.10.33 from "de Finibus Bonorum et Malorum" by Cicero are also reproduced in their exact original form, accompanied by English versions from the 1914 translation by H. Rackham</p>
    <p>The standard chunk of Lorem Ipsum used since the 1500s is reproduced below for those interested. Sections 1.10.32 and 1.10.33 from "de Finibus Bonorum et Malorum" by Cicero are also reproduced in their exact original form.</p>
  </div>
  <div class="signature" role="img" aria-label="Handwritten signature"></div>

  <div class="socials">
    <span><i class="ico"></i>Solvane-Harbor</span>
    <span><i class="ico"></i>@Solvaneharborca</span>
    <span><i class="ico"></i>@Solvaneharborco</span>
  </div>
  <div class="rule"></div>
  <div class="web">www.solvane-harbor.ca</div>
  <div class="band"></div>
</section>

<section class="card card-back">
  <div class="brand">
    <span class="brand-dot"></span>
    <span class="brand-name">SOLVANE-HARBOR</span>
  </div>
  <div class="web">www.solvane-harbor.ca</div>
</section>

<section class="card card-front">
  <div class="top-band"></div>
  <div class="top-line"></div>
  <div class="brand">
    <span class="brand-dot"></span>
    <div>
      <div class="brand-name">SOLVANE-HARBOR</div>
      <div class="brand-tag">CLARITY - GROWTH - PURPOSE</div>
    </div>
  </div>
  <div class="contact">
    <b>Mireille Dostana</b>
    MBA, MA, Beng, PCC<br>
    Business &amp; Corporate<br>
    <span>1 800 55 Canada <i class="ico"></i></span>
    <span>mireille@solvane-harbor.ca <i class="ico"></i></span>
  </div>
  <div class="socials">
    <span><i class="ico"></i>Solvane-Harbor</span>
    <span><i class="ico"></i>@Solvaneharborco</span>
    <span><i class="ico"></i>@Solvaneharborca</span>
  </div>
  <div class="rule"></div>
  <div class="tagline">Conscious Leadership Coaching</div>
  <div class="band"></div>
</section>

</body>
</html>
```